Attract customers for New Zealand forest eco tour

Website design for a new eco tourism business in New Zealand. We have domain name booked for it: www.GlenofTavi.co.nz

We have written the site, see attachments. And have all the pictures to go with it, have just attached a few of these for examples. Will provide the rest to the winning bidder.

We want the look of the site to be highly visually attractive, clean and uncluttered. And if you know about what works best for eco-tourism, that will help.

Website should be mobile phone readable, as well as desktop.

Our objectives for the site are to introduce our forest to them, get people interested in visiting, and have people book trips. We will need some kind of booking app such as with dates of bookings, and ideally a payment app as well so they can pay for bookings.

Ideally, I don't know if you can do this, you use a format which allows us to self edit the site (note, we're not technical experts).

Target Market(s)

Professional people aged 30 - 49.
Looking to travel, probably as a couple.
International travel for adventure, relaxation.

Key things they want are:

See attractions
Go to a place different from their own country
Escape from their usual working life
Unwind and relax

Industry/Entity Type

Business

Coding

Coded - Design and coding required

Number of Pages Required

5+ page

Colors
9bcb3b

Requirements
Must have
• Visually attractive - pictorial look
• Clean and uncluttered - blank space
• Mobile readable and desktop
• Booking app
• Payment app
Nice to have
• Be self editable by us (non-technical people)
Should not have
• shouldn't look cheap

```html
<!DOCTYPE html>
<html lang="en">
<head>
<meta charset="utf-8">
<title>Glen of Tavi</title>
<link rel="stylesheet" href="https://fonts.googleapis.com/css2?family=Open+Sans:wght@400;600;700&family=Source+Sans+3:wght@400;600;700&display=swap">
<style>
:root{
  --green:#9bcb3b;
  --green-dark:#7fae24;
  --orange:#e8600c;
  --orange-soft:#f07a22;
  --ink:#333;
  --muted:#777;
  --dark:#1e1e1e;
  --panel:#4a4a4a;
  --white:#fff;
  --light:#f2f2f2;
}
*{box-sizing:border-box;margin:0;padding:0}
html,body{width:1200px;height:3068px;overflow:hidden}
body{font-family:"Open Sans",sans-serif;color:var(--ink);background:var(--white);position:relative}
.abs{position:absolute}
h1,h2,h3{font-family:"Source Sans 3",sans-serif}

/* header / hero */
.hero{left:0;top:0;width:1200px;height:560px;background:linear-gradient(180deg,#2a3a36 0%,#3d5a57 35%,#5f7d6c 60%,#2c3a2a 100%)}
.site-name{left:108px;top:14px;font-family:"Source Sans 3",sans-serif;font-weight:700;font-size:40px;color:var(--green)}
.nav{right:120px;top:26px;display:flex;gap:30px;font-size:15px;color:var(--white)}
.nav .active{color:var(--green)}
.welcome{left:0;width:1200px;top:176px;text-align:center;color:var(--white)}
.welcome h1{font-size:44px;font-weight:700}
.welcome p{font-size:20px;margin-top:4px}
.btn-outline{display:inline-block;margin-top:26px;border:2px solid var(--green);color:var(--white);font-size:14px;padding:6px 28px}

/* booking row */
.book{left:112px;top:452px;width:304px;height:388px;background:var(--panel);border:4px solid var(--green)}
.book h2{background:var(--green);color:var(--white);font-size:30px;padding:10px 18px}
.book form{padding:10px 18px}
.book small{color:#ddd;font-size:11px}
.book .field{background:var(--white);height:26px;margin-top:8px;font-size:11px;color:#999;padding:5px 8px}
.book .field.tall{height:70px}
.book .submit{margin:14px auto 0;width:160px;height:34px;background:var(--orange);color:var(--white);font-weight:700;text-align:center;line-height:34px;font-size:15px}
.tour{width:304px;height:388px;top:452px;background:var(--panel)}
.tour .photo{height:268px}
.tour h3{color:var(--white);font-size:16px;padding:14px 14px 6px;font-weight:600}
.tour .read{left:14px;bottom:22px;background:var(--orange);color:var(--white);font-size:13px;padding:5px 14px}
.tour .price{right:16px;bottom:16px;color:var(--green);font-size:32px;font-weight:700;font-family:"Source Sans 3",sans-serif}

/* project */
.project-photo{left:0;top:888px;width:600px;height:432px;background:radial-gradient(circle at 40% 55%,#3f5a2a 0%,#5a3a2a 45%,#9a8d84 100%)}
.project{left:600px;top:888px;width:600px;height:432px;background:var(--green);color:var(--white);padding:60px 56px 0 44px}
.project h2{font-size:38px;font-weight:700}
.project .lead{font-size:17px;font-weight:600;margin-top:4px;line-height:1.25}
.project .body{font-size:12px;line-height:1.55;margin-top:18px}
.btn-orange{display:inline-block;background:var(--orange);color:var(--white);font-size:14px;padding:8px 22px;margin-top:22px}

/* activities */
.section-title{left:0;width:1200px;text-align:center;color:var(--orange);font-size:38px;font-weight:700}
.section-sub{left:0;width:1200px;text-align:center;font-size:15px;line-height:1.35}
.activity{width:220px;text-align:center}
.activity .icon{width:120px;height:120px;border-radius:50%;background:var(--orange);margin:0 auto}
.activity p{font-size:14px;font-weight:700;margin-top:10px;text-transform:uppercase;line-height:1.25}

/* attractions */
.attractions{left:0;top:1920px;width:1200px;height:440px;background:linear-gradient(90deg,#3a2a20,#6a4c38 40%,#4b3a2e 70%,#2c2420)}
.attractions .title{color:var(--white);font-size:38px;top:26px}
.attractions .sub{color:var(--white);top:74px}
.attr-card{top:140px;width:304px;height:220px;background:linear-gradient(180deg,#8a8f92,#4a4a48)}
.attr-card .tag{left:0;top:8px;background:#1a70b8;color:var(--white);font-size:13px;font-weight:700;padding:4px 10px}
.attr-card .cap{left:0;bottom:0;width:100%;background:rgba(0,0,0,.55);color:var(--white);font-size:22px;padding:10px 14px}
.attr-card .days{right:14px;bottom:14px;width:68px;height:68px;border-radius:50%;background:var(--orange);color:var(--white);text-align:center;font-weight:700;font-size:18px;line-height:1;padding-top:14px}
.attr-card .days span{display:block;font-size:12px;margin-top:3px}

/* contact */
.contact .label{color:var(--orange);font-size:15px;font-weight:600}
.contact .value{font-size:11px;line-height:1.5;color:#555}
.input{background:var(--light);height:44px;border:1px solid #ddd}
.send{border:2px solid var(--orange);color:var(--orange);font-size:13px;padding:8px 20px}

.map{left:0;top:2732px;width:1200px;height:248px;background:linear-gradient(135deg,#cfd9c0,#e4e8dc 50%,#c5d2bb)}
.footer{left:0;top:2980px;width:1200px;height:88px;background:var(--dark);color:#ccc;font-size:14px}
.footer .copy{left:112px;top:34px}
.social{right:112px;top:24px;display:flex;gap:8px}
.social span{width:38px;height:38px;background:#3c6fb4}
</style>
</head>
<body>

<header class="hero abs" role="img" aria-label="Coastal forest and hills of the Far North at dusk">
</header>
<div class="site-name abs">Glen of Tavi</div>
<nav class="nav abs">
  <span class="active">Home</span><span>About Us</span><span>Tours</span><span>Project</span><span>Activities</span><span>Gallery</span><span>Contact US</span>
</nav>
<div class="welcome abs">
  <h1>welcome to our site</h1>
  <p>Glen of Tavi is a beautiful native forest in the Far North of New Zealand</p>
  <span class="btn-outline">Learn more</span>
</div>

<section class="book abs">
  <h2>Book Now</h2>
  <form>
    <small>*All fields are required</small>
    <div class="field">First name</div>
    <div class="field">Last name</div>
    <div class="field">Email address</div>
    <div class="field">Phone Number</div>
    <div class="field tall">Message</div>
    <div class="submit">SUBMIT</div>
  </form>
</section>
<article class="tour abs" style="left:448px">
  <div class="photo" role="img" aria-label="Tent lit up under a night sky" style="background:linear-gradient(180deg,#0c1a40,#1c4ab0 60%,#101830)"></div>
  <h3>OVERNIGHT TOURS</h3>
  <span class="read abs">Read more</span><span class="price abs">$100</span>
</article>
<article class="tour abs" style="left:784px">
  <div class="photo" role="img" aria-label="Family walking a forest trail" style="background:linear-gradient(180deg,#c9d6c6,#8a9a70 55%,#6e6248)"></div>
  <h3>DAY TRIPS</h3>
  <span class="read abs">Read more</span><span class="price abs">$100</span>
</article>

<div class="project-photo abs" role="img" aria-label="Red forest berries among green leaves"></div>
<section class="project abs">
  <h2>OUR PROJECT</h2>
  <p class="lead">In the Far North, West, of New Zealand the climate is warm and very wet in Winter.</p>
  <p class="body">The forest is rich with life, and visitors come to find a quiet corner of nature. Trees are old and tall. Birds call from dawn to dusk, and streams run clear between the ferns. We care for this land so each guest can walk it, learn from it and leave it as it was found. Our guides share local stories, plant lore and the history of the valley on every trip.</p>
  <span class="btn-orange">Read more</span>
</section>

<h2 class="section-title abs" style="top:1364px">OUR ACTIVITIES</h2>
<p class="section-sub abs" style="top:1416px">You can do what you like as activities. These are some of things we enjoy, and visitors to the forest<br>we've had really.</p>
<div class="activity abs" style="left:118px;top:1482px"><div class="icon" role="img" aria-label="Old tree icon"></div><p>Grandfather of the<br>forest</p></div>
<div class="activity abs" style="left:366px;top:1482px"><div class="icon" role="img" aria-label="Owl icon"></div><p>Birdwatcher</p></div>
<div class="activity abs" style="left:614px;top:1482px"><div class="icon" role="img" aria-label="Food bowl icon"></div><p>Forest gourmet</p></div>
<div class="activity abs" style="left:862px;top:1482px"><div class="icon" role="img" aria-label="Crayfish icon"></div><p>Crayfish hunter</p></div>
<div class="activity abs" style="left:118px;top:1672px"><div class="icon" role="img" aria-label="Walker icon"></div><p>Forestman</p></div>
<div class="activity abs" style="left:366px;top:1672px"><div class="icon" role="img" aria-label="Orchid flower icon"></div><p>Orchid obsessive</p></div>
<div class="activity abs" style="left:614px;top:1672px"><div class="icon" role="img" aria-label="Spider icon"></div><p>Purupi giant legs</p></div>
<div class="activity abs" style="left:862px;top:1672px"><div class="icon" role="img" aria-label="Pine trees icon"></div><p>Tree guru</p></div>

<section class="attractions abs" role="img" aria-label="Blurred forest landscape background">
  <h2 class="section-title abs title">LOCAL ATTRACTIONS</h2>
  <p class="section-sub abs sub">If you're coming to this part of the country, there are some awesome local attractions nearby</p>
  <div class="attr-card abs" style="left:112px" role="img" aria-label="Rock arch over the sea"><span class="tag abs">$7,001</span><div class="cap abs">Lorem ipsum dolor</div><div class="days abs">15<span>DAYS</span></div></div>
  <div class="attr-card abs" style="left:448px" role="img" aria-label="Rock arch over the sea"><span class="tag abs">$7,001</span><div class="cap abs">Lorem ipsum dolor</div><div class="days abs">15<span>DAYS</span></div></div>
  <div class="attr-card abs" style="left:784px" role="img" aria-label="Rock arch over the sea"><span class="tag abs">$7,001</span><div class="cap abs">Lorem ipsum dolor</div><div class="days abs">15<span>DAYS</span></div></div>
</section>

<section class="contact">
  <h2 class="section-title abs" style="top:2400px;color:var(--ink);font-weight:600">CONTACT US</h2>
  <div class="label abs" style="left:112px;top:2472px">Our Address</div>
  <div class="value abs" style="left:264px;top:2470px">Lorem ipsum dolor sit amet,<br>consectetur adipiscing elit.</div>
  <div class="label abs" style="left:112px;top:2576px">Phone Number</div>
  <div class="value abs" style="left:264px;top:2574px">0800 555 0142<br>0800 555 0143</div>
  <div class="label abs" style="left:112px;top:2630px">Email Id</div>
  <div class="value abs" style="left:264px;top:2628px">info@email.com<br>admin@email.com</div>
  <div class="input abs" style="left:448px;top:2466px;width:304px"></div>
  <div class="input abs" style="left:784px;top:2466px;width:304px"></div>
  <div class="input abs" style="left:448px;top:2526px;width:640px;height:160px"></div>
  <span class="send abs" style="left:888px;top:2672px;background:#fff">Send a Message</span>
</section>

<div class="map abs" role="img" aria-label="Map of the Far North region"></div>

<footer class="footer abs">
  <span class="copy abs">Copyright © 2015 lorem ipsum dolor</span>
  <div class="social abs"><span></span><span></span><span></span><span></span></div>
</footer>

</body>
</html>
```